依頼詳細
◆ディナーショー詳細

・鳴瀬野ガーデンホテル(かつて天皇陛下も宿泊された、格式&レトロ感のあるホテル)にて開催。ディナーはフランス料理
・ショー第1部:二胡と箏(着物ドレス着用)(和風の音楽でスタート)
第2部:二胡とピアノ(カクテルドレス)
(生命の息吹を感じる季節・コロナも明けて・自身の九死に一生を得た体験を含めて、生きる歓びを語るようなトークを交えて)
第3部:二胡とソノリカ(トレーンの長いゴージャスなドレス)
(プロジェクターを使用し、画像や動画で世界観を演出)
・紅茶コンサルタントが、コース一品ずつに合わせ、料理に合う紅茶を提供
・ホテル本館2階ラウンジからは、海に浮かぶ「竹島」の絶景が眺められる。
17時よりラウンジにて、夕陽に染まる絶景を見ながらウェルカムドリンクを嗜んでいただく。
宴会場へ移動し、18時よりショースタート。
・桜の咲く時期を選んで開催

◆デザイン要望

・上記のディナーショーがイメージできるようなデザイン
もしくは
チラシを一枚見るだけで「どんなショーなのだろう?」とディナーショーへ期待の膨らむようなデザイン
(・・・でありながら、主役がぼけないチラシ)が希望です。
記載項目
掲載内容のテキストは、添付のエクセルファイルをご参照ください。ページ内に、宣材写真のダウンロードURLも貼ってありますので、写真はそこからご使用ください。(写真の使用枚数等こだわりはありません)
サイズ
A4
ページ数
片面
希望イメージ
シンプル 複雑
単色 カラフル
暗い 明るい
日常 高級
遊び心 厳粛
未来的 伝統的
女性的 男性的
希望する色
設定なし
納品ファイル
• 高解像度JPG (.jpg)
• PNG形式 (.png)
補足説明
・もし可能でしたら、印刷(コピエールやモナリト等)入稿まで行っていただくか、入稿方法をご指南いただけると助かります。印刷費用については、別途予算を組んでおります。
・今回依頼が初めてで不慣れな点が多々あります。ご不明な点やご指摘等ありましたら、仰っていただけますようよろしくお願いいたします。
■ 選んだ理由

素敵な作品を沢山ご提案いただき、私としては絞りきれず、とても迷ってしまいました。そこで、家族やディナーショーの協力者、スタッフなど、複数の方に相談したところ、多数決で柚木様のデザインに票が集まり、決定させていただきました。全体的に優しい色味で文字も見やすく、気に入っています。

■ 提案者全員のお礼・コメント

この度は沢山のご提案をいただき、本当にありがとうございました。ご提案をいただく度に、A4用紙一枚に込められたデザインの多様性やデザイナーさんの思い、一瞬にしてインパクトを与えるチラシデザインの奥深さに感動して、何度か目が潤んでしまいました。できれば部屋に飾っておきたい作品もありましたが、そういう選択ができないのが残念です。また依頼させていただく際には、よろしくお願い致します。

```html
<!DOCTYPE html>
<html lang="ja">
<head>
<meta charset="utf-8">
<title>小坂梨奈 スプリングディナーショー</title>
<link href="https://fonts.googleapis.com/css2?family=Great+Vibes&family=Shippori+Mincho:wght@500;600&family=Noto+Serif+JP:wght@400;500&display=swap" rel="stylesheet">
<style>
  :root {
    --paper: #fffdfb;
    --rose: #c0707f;
    --rose-deep: #a85d6d;
    --ink: #5a4a4e;
    --hero-top: #f6d6dc;
    --hero-mid: #f1b9b4;
    --hero-low: #f2a98a;
    --white: #ffffff;
  }
  * { margin: 0; padding: 0; box-sizing: border-box; }
  html, body { width: 848px; height: 1200px; overflow: hidden; background: var(--paper); }
  .flyer { position: relative; width: 848px; height: 1200px; background: var(--paper); font-family: "Noto Serif JP", serif; color: var(--ink); }

  .hero {
    position: absolute; left: 0; top: 0; width: 848px; height: 710px;
    background:
      radial-gradient(ellipse 320px 420px at 430px 330px, #fbe8e6 0%, rgba(251,232,230,0) 70%),
      linear-gradient(180deg, var(--hero-top) 0%, var(--hero-mid) 45%, var(--hero-low) 78%, var(--paper) 100%);
  }
  .hero-copy {
    position: absolute; left: 48px; top: 40px; height: 240px;
    writing-mode: vertical-rl; font-size: 13px; line-height: 26px; letter-spacing: 3px; color: var(--white);
  }
  .hero-script {
    position: absolute; left: 520px; top: 300px; width: 320px;
    font-family: "Great Vibes", cursive; color: var(--white); font-size: 50px; line-height: 58px;
    transform: rotate(-8deg); text-shadow: 0 0 6px rgba(200,120,130,.35);
  }
  .hero-script span { display: block; }
  .hero-script .l2 { padding-left: 40px; }
  .hero-script .l3 { padding-left: 90px; }

  .title { position: absolute; left: 0; top: 712px; width: 848px; text-align: center; font-family: "Shippori Mincho", serif; color: var(--rose); font-weight: 600; }
  .title .name { font-size: 60px; line-height: 72px; letter-spacing: 6px; }
  .title .show { font-size: 58px; line-height: 70px; letter-spacing: 2px; }
  .event-line { position: absolute; left: 0; top: 862px; width: 848px; text-align: center; font-family: "Shippori Mincho", serif; color: var(--rose); font-size: 30px; letter-spacing: 1px; }
  .event-line .venue { margin-left: 18px; }
  .event-line .mark { display: inline-block; width: 18px; height: 18px; border-radius: 50%; border: 1.5px solid var(--rose); margin-left: 10px; vertical-align: 4px; }

  .gallery { position: absolute; left: 150px; top: 912px; width: 548px; display: flex; gap: 4px; }
  .gallery div { width: 134px; height: 74px; }
  .g-hotel { background: linear-gradient(180deg, #9cc3dd, #6d8f6a); }
  .g-dinner { background: linear-gradient(180deg, #8c6a54, #d8b89a); }
  .g-tea { background: linear-gradient(180deg, #e9ddd2, #b58560); }
  .g-hall { background: linear-gradient(180deg, #3a3f66, #b4708a); }

  .details { position: absolute; left: 206px; top: 1008px; width: 440px; font-size: 11px; line-height: 19px; }
  .row { display: flex; }
  .row dt { width: 96px; color: var(--rose-deep); }
  .row dd { flex: 1; }
  .row + .row { margin-top: 8px; }
  .sched span { display: inline-block; width: 118px; }
</style>
</head>
<body>
<main class="flyer">
  <section class="hero" role="img" aria-label="春の桜の花びらが舞う夕景を背に、白いドレスで二胡を奏でる演奏者の写真">
    <p class="hero-copy">春の風に誘われて 二胡の調べが響く<br>桜舞う夕べ 海を望む特別な時間<br>あなたを優雅な世界へご招待します</p>
    <p class="hero-script"><span class="l1">Rina Kosaka</span><span class="l2">Spring</span><span class="l3">Diner Show</span></p>
  </section>

  <h1 class="title">
    <span class="name">小坂梨奈</span><br>
    <span class="show">スプリングディナーショー</span>
  </h1>
  <p class="event-line">2022年4月3日(日)<span class="venue">鳴瀬野ガーデンホテル</span><span class="mark"></span></p>

  <div class="gallery">
    <div class="g-hotel" role="img" aria-label="海辺に建つホテルの外観写真"></div>
    <div class="g-dinner" role="img" aria-label="ダイニングでのフランス料理の写真"></div>
    <div class="g-tea" role="img" aria-label="紅茶のカップの写真"></div>
    <div class="g-hall" role="img" aria-label="ライトアップされた宴会場の写真"></div>
  </div>

  <dl class="details">
    <div class="row sched"><dt>タイムスケジュール</dt><dd><span>ウェルカムドリンク</span>17:00〜　本館ラウンジにて<br><span>ショー&amp;ディナー</span>18:00〜　宴会場にて</dd></div>
    <div class="row"><dt>料　金</dt><dd>お一人様　27,000円(税・サービス料込)</dd></div>
    <div class="row"><dt>ご予約・お問い合わせ</dt><dd>メール　hello@rinakosaka.example<br>ＵＲＬ　https://rinakosaka.example/concert/</dd></div>
  </dl>
</main>
</body>
</html>
```